Business cards and stationary for a new health advocacy nonprofit
Marlowe Harbor Wellness Union
Business cards and stationary for a new health advocacy nonprofit - Health
Creative Brief
Simple
Dana Pelliser
President & Founder
4521 E 87th St., Overland Park, KS 66219-2071
dpelliser@mhwunion.org
www.mhwunion.org
Connecting science, resources, and funding to the Turner Syndrome community
harborunionhq harborunionhq
We do not want the dark purple to be a dominant color in the design. Prefer the lighter shade of purple. Thank you.
We definitely like the lighter purple in #8 and #9 not the dark shade. Like some of your ideas, but it is also only the first day to the contest so we do not yet feel we have enough samples to look at. Thank you.

```html
<!DOCTYPE html>
<html lang="en">
<head>
<meta charset="utf-8">
<title>Marlowe Harbor Wellness Union – Business Cards</title>
<link rel="stylesheet" href="https://fonts.googleapis.com/css2?family=Open+Sans:wght@400;600;700&display=swap">
<style>
  :root {
    --bg: #d9d9db;
    --card: #ffffff;
    --purple: #8a3aa6;
    --purple-deep: #6f2a8c;
    --pink: #d13a8e;
    --ink: #3a3a3a;
    --white: #ffffff;
  }
  * { box-sizing: border-box; margin: 0; padding: 0; }
  html, body {
    width: 1200px; height: 895px; overflow: hidden;
    background: var(--bg);
    font-family: "Open Sans", Arial, sans-serif;
  }
  .stage { position: relative; width: 1200px; height: 895px; }
  .card {
    position: absolute; top: 290px;
    width: 540px; height: 310px;
    background: var(--card);
    border-radius: 4px;
    box-shadow: 0 2px 6px rgba(0,0,0,0.12);
    overflow: hidden;
  }
  .card--front { left: 40px; }
  .card--back { left: 620px; }

  .brand { display: flex; align-items: center; gap: 10px; }
  .brand__dot {
    width: 34px; height: 34px; border-radius: 50%;
    background: var(--purple); flex: none;
  }
  .brand__name {
    color: var(--purple);
    font-weight: 700;
    font-size: 19px;
    line-height: 1.1;
    max-width: 230px;
  }

  /* Back side */
  .card--back .brand { position: absolute; left: 250px; top: 96px; }
  .web-pill {
    position: absolute; left: 0; top: 168px;
    width: 230px; height: 30px;
    background: var(--pink);
    border-radius: 0 15px 15px 0;
    color: var(--white);
    font-size: 14px; font-weight: 600;
    display: flex; align-items: center;
    padding-left: 22px;
  }

  /* Front side */
  .card--front .brand { position: absolute; left: 30px; top: 32px; }
  .contact-head {
    position: absolute; left: 30px; top: 118px;
    display: flex; align-items: baseline; gap: 8px;
    color: var(--ink);
  }
  .person { font-size: 21px; font-weight: 600; }
  .divider { font-size: 22px; font-weight: 400; }
  .role { font-size: 16px; font-weight: 400; }
  .address {
    position: absolute; left: 30px; top: 156px;
    font-size: 13px; color: var(--ink); font-weight: 600;
  }
  .contact-bar {
    position: absolute; left: 0; top: 186px;
    width: 440px; height: 28px;
    background: var(--purple);
    display: flex; align-items: center; gap: 18px;
    padding-left: 24px;
    color: var(--white); font-size: 12.5px; font-weight: 600;
  }
  .email-pill {
    position: absolute; left: 330px; top: 212px;
    width: 210px; height: 28px;
  }
  .email-bar {
    position: absolute; left: 300px; top: 214px;
    width: 230px; height: 28px;
    background: var(--purple);
    border-radius: 0 14px 14px 0;
    display: flex; align-items: center; gap: 6px;
    padding-left: 14px;
    color: var(--white); font-size: 12.5px; font-weight: 600;
  }
  .contact-item { display: flex; align-items: center; gap: 6px; }
  .icon { width: 14px; height: 14px; flex: none; }
</style>
</head>
<body>
<main class="stage">

  <section class="card card--front" aria-label="Business card front">
    <div class="brand">
      <span class="brand__dot"></span>
      <span class="brand__name">Marlowe Harbor Wellness Union</span>
    </div>
    <div class="contact-head">
      <span class="person">Dana Pelliser</span>
      <span class="divider">|</span>
      <span class="role">President &amp; Ceo</span>
    </div>
    <p class="address">4521 E 87th St., Overland Park, KS 66219-2071</p>
    <div class="contact-bar">
      <span class="contact-item">
        <svg class="icon" viewBox="0 0 14 14"><circle cx="7" cy="7" r="7" fill="#fff"/><path d="M4.3 3.6l1.4-.3.7 1.7-.9.6c.4.9 1 1.5 1.9 1.9l.6-.9 1.7.7-.3 1.4c-3 .1-5.2-2.1-5.1-5.1z" fill="#8a3aa6"/></svg>
        555 014 2290
      </span>
      <span class="contact-item">
        <svg class="icon" viewBox="0 0 14 14"><circle cx="7" cy="7" r="7" fill="#fff"/><path d="M4.3 3.6l1.4-.3.7 1.7-.9.6c.4.9 1 1.5 1.9 1.9l.6-.9 1.7.7-.3 1.4c-3 .1-5.2-2.1-5.1-5.1z" fill="#8a3aa6"/></svg>
        555 014 2291
      </span>
    </div>
    <div class="email-bar">
      <svg class="icon" viewBox="0 0 14 14"><circle cx="7" cy="7" r="7" fill="#fff"/><rect x="3.5" y="4.5" width="7" height="5" fill="none" stroke="#8a3aa6" stroke-width="1"/><path d="M3.5 4.5L7 7.3l3.5-2.8" fill="none" stroke="#8a3aa6" stroke-width="1"/></svg>
      dpelliser@mhwunion.org
    </div>
  </section>

  <section class="card card--back" aria-label="Business card back">
    <div class="web-pill">www.mhwunion.org</div>
    <div class="brand">
      <span class="brand__dot"></span>
      <span class="brand__name">Marlowe Harbor Wellness Union</span>
    </div>
  </section>

</main>
</body>
</html>
```